Boat business cards

I'm looking for business cards with the two logos I've attached. I don't have an specific idea in mind and open to anything. All the usual info will be on the card. Name, position in company, nr, email, address, ect. The company rents out these two boats for charters and fishing.

```html
<!DOCTYPE html>
<html lang="en">
<head>
<meta charset="utf-8">
<title>Harbor Light Charters – Business Cards</title>
<link rel="stylesheet" href="https://fonts.googleapis.com/css2?family=Mulish:wght@400;600;700&display=swap">
<style>
  :root {
    --stage: #141415;
    --card-dark: #2b2c30;
    --card-light: #ffffff;
    --accent-blue: #4f82d6;
    --text-light: #f2f2f2;
    --text-grey: #5d5f63;
    --rule: #55575c;
    --boat-sand: #9c7c55;
    --boat-sky: #8fb0e2;
  }
  * { box-sizing: border-box; margin: 0; padding: 0; }
  html, body {
    width: 1200px;
    height: 820px;
    overflow: hidden;
    background: var(--stage);
    font-family: "Mulish", Arial, sans-serif;
  }
  .card {
    position: absolute;
    top: 255px;
    width: 540px;
    height: 310px;
    border-radius: 2px;
  }

  /* Front card */
  .card--front {
    left: 40px;
    background: var(--card-dark);
    border-left: 3px solid var(--accent-blue);
    border-bottom: 3px solid var(--accent-blue);
    color: var(--text-light);
  }
  .brand {
    position: absolute;
    left: 200px;
    top: 40px;
    width: 300px;
    text-align: center;
  }
  .brand__art {
    display: block;
    width: 230px;
    height: 70px;
    margin: 0 auto 10px;
    border-radius: 4px;
    background: linear-gradient(180deg, #d9dadd 0%, var(--boat-sand) 70%, #34405a 100%);
  }
  .brand__name {
    font-size: 30px;
    font-weight: 700;
    letter-spacing: 2px;
    color: var(--text-light);
    text-transform: uppercase;
  }
  .divider {
    position: absolute;
    left: 210px;
    right: 30px;
    top: 190px;
    height: 1px;
    background: var(--rule);
  }
  .person {
    position: absolute;
    left: 34px;
    top: 168px;
  }
  .person__name {
    font-size: 22px;
    font-weight: 600;
    color: var(--accent-blue);
    text-transform: uppercase;
    letter-spacing: 0.5px;
  }
  .person__role {
    font-size: 14px;
    margin-top: 1px;
  }
  .contacts {
    position: absolute;
    left: 40px;
    top: 228px;
    list-style: none;
    font-size: 14px;
    line-height: 22px;
  }
  .contacts li { display: flex; align-items: center; gap: 9px; }
  .contacts svg { width: 14px; height: 14px; flex: none; }
  .address {
    position: absolute;
    right: 34px;
    top: 206px;
    text-align: right;
    font-size: 13px;
    line-height: 18px;
  }

  /* Back card */
  .card--back {
    left: 620px;
    background: var(--card-light);
    border-bottom: 5px solid var(--accent-blue);
  }
  .back-brand {
    position: absolute;
    left: 0; right: 0;
    top: 70px;
    text-align: center;
  }
  .back-brand__art {
    display: block;
    width: 280px;
    height: 100px;
    margin: 0 auto 14px;
    border-radius: 4px;
    background: linear-gradient(180deg, #eef1f6 0%, var(--boat-sky) 100%);
  }
  .back-brand__name {
    font-size: 34px;
    font-weight: 700;
    color: var(--text-grey);
    text-transform: uppercase;
    letter-spacing: 2px;
  }
</style>
</head>
<body>
  <section class="card card--front">
    <div class="brand">
      <span class="brand__art" role="img" aria-label="Illustration of a motor yacht on the water"></span>
      <div class="brand__name">Harbor Light</div>
    </div>
    <div class="divider"></div>
    <div class="person">
      <div class="person__name">Jonathan Smith</div>
      <div class="person__role">Managing Director</div>
    </div>
    <ul class="contacts">
      <li>
        <svg viewBox="0 0 16 16" aria-hidden="true"><path fill="#4f82d6" d="M4 1l2.5 3-1.5 1.5c.8 2 2.5 3.7 4.5 4.5L11 8.5 14 11l-1.5 3C7 14 2 9 2 2.5z"/></svg>
        044-123 456 789
      </li>
      <li>
        <svg viewBox="0 0 16 16" aria-hidden="true"><rect x="1" y="3" width="14" height="10" fill="#4f82d6"/><path d="M1 3l7 6 7-6" fill="none" stroke="#2b2c30" stroke-width="1.3"/></svg>
        info@webname.com
      </li>
      <li>
        <svg viewBox="0 0 16 16" aria-hidden="true"><g fill="none" stroke="#4f82d6" stroke-width="1.4"><circle cx="8" cy="8" r="6.5"/><ellipse cx="8" cy="8" rx="3" ry="6.5"/><path d="M1.5 8h13M3 4.5h10M3 11.5h10"/></g></svg>
        www.websitename.com
      </li>
    </ul>
    <address class="address" style="font-style:normal">
      421, Address line goes here<br>45452, Country Name
    </address>
  </section>

  <section class="card card--back">
    <div class="back-brand">
      <span class="back-brand__art" role="img" aria-label="Illustration of a sport fishing boat"></span>
      <div class="back-brand__name">Sea Breeze 42</div>
    </div>
  </section>
</body>
</html>
```